Tampa Bay fishing guide needs stunning website.

I currently have a site - www.reelcoveguide.example which I personally put together using the Plixo platform and I am looking for a redesign on a different platform (Brindlepress?) that will allow me to easily create landing pages in the future. Would like to have a block for visitors to opt in to newsletter. Need social media links on all pages.
Updates

I would like to let my visitors know that I am able to handle their fishing charter needs here in the Tampa Bay area, if I'm not available for the dates they are looking to go I can refer them to a reputable captain in the area.

Target Market(s)

United States

Industry/Entity Type

Tourism

Coding

Coded - Design and coding required

Number of Pages Required

5+ page

Font styles to use
Sans Serif

Colors
0355a3
3176b5
85abd2
fbf289

Requirements
Must have
• Mobile Responsive, Ability to insert Vantor Metrics, Quillbook pixels, ability to add custom landing pages in future
Nice to have
• Clean, easy navigation

```html
<!DOCTYPE html>
<html lang="en">
<head>
<meta charset="utf-8">
<title>Capt. Wade Harlow – Tampa Bay Fishing Charters</title>
<link rel="stylesheet" href="https://fonts.googleapis.com/css2?family=Raleway:wght@400;500;600&family=Open+Sans:wght@400;600&display=swap">
<style>
:root{
  --blue-deep:#0355a3;
  --blue:#1f5fae;
  --blue-mid:#3176b5;
  --blue-soft:#85abd2;
  --yellow:#fbf289;
  --yellow-dark:#e8d96a;
  --ink:#2b2b2b;
  --muted:#666;
  --footer:#0d1621;
  --footer-base:#0a1019;
  --paper:#f3f3f3;
}
*{box-sizing:border-box;margin:0;padding:0}
html,body{width:680px;height:1200px;overflow:hidden}
body{font-family:"Open Sans",sans-serif;color:var(--ink);background:#fff;position:relative}
.hero{position:absolute;left:0;top:0;width:680px;height:359px;background:linear-gradient(135deg,#6e6a55 0%,#8a7a62 35%,#4a4a3a 70%,#6b6d58 100%)}
.hero-photo{position:absolute;inset:0}
.slider-arrow{position:absolute;top:223px;width:12px;height:12px;border-radius:50%;background:rgba(0,0,0,.45)}
.slider-arrow.prev{left:16px}.slider-arrow.next{left:652px}
.topbar{position:absolute;left:63px;top:0;width:554px;height:65px;background:rgba(246,246,246,.96);display:flex;justify-content:space-between;align-items:center;padding:0 15px 0 14px}
.brand{font-family:"Raleway",sans-serif;font-weight:600;font-size:19px;color:var(--blue-deep);display:flex;align-items:center;gap:6px}
.brand-dot{width:10px;height:10px;border-radius:50%;background:var(--blue-mid)}
.call{display:flex;align-items:center;gap:6px}
.call-label{font-size:9px;color:var(--muted);line-height:1}
.call-number{font-size:15px;color:#222;line-height:1.2}
.nav{position:absolute;left:63px;top:65px;width:554px;height:35px;background:var(--blue-deep);display:flex;align-items:center;justify-content:space-between;padding:0 33px 0 20px}
.nav a{font-family:"Raleway",sans-serif;font-weight:600;font-size:7px;color:#fff;text-decoration:none;letter-spacing:.2px}
.nav a.active{background:var(--yellow);color:var(--blue-deep);padding:7px 15px;border-radius:12px}
.hero-caption{position:absolute;left:63px;top:286px;width:377px;height:73px;background:rgba(3,85,163,.85);padding:20px 24px;font-family:"Raleway",sans-serif;font-weight:500;font-size:10.5px;line-height:19px;color:#fff}
.intro{position:absolute;left:0;top:359px;width:680px;height:248px;background:linear-gradient(135deg,#f8f8f8,#ececec 50%,#f7f7f7);text-align:center}
.intro h1{margin-top:68px;font-family:"Raleway",sans-serif;font-weight:400;font-size:15px;letter-spacing:3.4px;line-height:25px;color:#222}
.intro p{font-size:6.3px;line-height:14.5px;color:#555;width:540px;margin:10px auto 0}
.intro p a{color:var(--blue-deep);text-decoration:none}
.services{position:absolute;left:0;top:607px;width:680px;height:397px;background:linear-gradient(180deg,#0d4fa0 0%,#1a5fae 55%,#2a6db5 100%)}
.card{position:absolute;top:73px;width:270px;height:263px;background:#fff}
.card.charters{left:63px}.card.pickups{left:347px}
.card h2{font-family:"Raleway",sans-serif;font-weight:500;font-size:15px;color:#222;padding:13px 15px 0;height:42px}
.card-photo{height:122px;background:linear-gradient(135deg,#1f7a6a,#2a8f8a 40%,#d8d8d8 70%,#f2f2f2)}
.pickups .card-photo{background:linear-gradient(135deg,#0f2c3a,#2d5670 45%,#e6eef3 75%,#ffffff)}
.card p{font-size:6.3px;line-height:14.5px;color:#555;padding:13px 16px 0}
.btn{position:absolute;left:16px;top:230px;height:22px;padding:0 13px;border-radius:11px;background:var(--yellow);font-family:"Raleway",sans-serif;font-weight:600;font-size:7px;color:var(--blue-deep);display:flex;align-items:center;gap:4px;box-shadow:0 1px 2px rgba(0,0,0,.2)}
.footer{position:absolute;left:0;top:1004px;width:680px;height:142px;background:var(--footer)}
.footer h3{font-family:"Raleway",sans-serif;font-weight:500;font-size:12px;color:#fff;margin-bottom:10px}
.col{position:absolute;top:32px}
.col.contact{left:63px}.col.pickup{left:226px;border-left:1px dashed #2a3440;padding-left:0}
.col.news{left:397px;width:220px}
.divider{position:absolute;top:30px;width:0;height:95px;border-left:1px dashed #283240}
.socials{display:flex;gap:4px;margin-bottom:12px}
.socials span{width:18px;height:18px;border-radius:50%;background:var(--yellow);font-size:7px;font-weight:600;color:var(--blue-deep);display:flex;align-items:center;justify-content:center}
.line{display:flex;align-items:center;gap:5px;font-size:6.3px;color:#dfe4ea;margin-bottom:12px}
.pickup-list{list-style:none}
.pickup-list li{font-size:6.3px;color:#dfe4ea;margin-bottom:12px;padding-left:7px;position:relative}
.pickup-list li::before{content:"";position:absolute;left:0;top:2px;border-left:3px solid #dfe4ea;border-top:2.5px solid transparent;border-bottom:2.5px solid transparent}
.news p{font-size:6.3px;line-height:14.5px;color:#dfe4ea}
.signup{display:flex;gap:8px;margin-top:8px}
.signup .email{width:132px;height:23px;border-radius:12px;background:#fff;font-size:6px;color:#999;padding:7px 10px}
.signup .submit{width:80px;height:23px;border-radius:12px;background:var(--yellow);font-family:"Raleway",sans-serif;font-weight:600;font-size:8px;color:var(--blue-deep);display:flex;align-items:center;justify-content:center}
.base{position:absolute;left:0;top:1146px;width:680px;height:54px;background:var(--footer-base)}
.copyright{position:absolute;left:63px;top:23px;font-size:6px;color:#cfd5dc}
.cards{position:absolute;right:63px;top:21px;display:flex;gap:6px}
.cards span{width:16px;height:10px;background:#555d66;font-size:3px;color:#e6e6e6;display:flex;align-items:center;justify-content:center}
</style>
</head>
<body>
<header class="hero">
  <div class="hero-photo" role="img" aria-label="Close-up photo of a bass leaping from the water with a lure in its mouth"></div>
  <span class="slider-arrow prev"></span><span class="slider-arrow next"></span>
  <div class="topbar">
    <div class="brand"><span class="brand-dot"></span>Capt. Wade Harlow</div>
    <div class="call">
      <svg width="22" height="22" viewBox="0 0 24 24"><path d="M6 3l3 5-2 2c1 3 3 5 6 6l2-2 5 3-2 4C10 21 3 14 2 6z" fill="#0355a3"/></svg>
      <div><div class="call-label">Call Us :</div><div class="call-number">555-014-2280</div></div>
    </div>
  </div>
  <nav class="nav">
    <a class="active" href="#">HOME</a><a href="#">ABOUT US</a><a href="#">PICK UP LOCATIONS</a><a href="#">RATES</a><a href="#">CONTACT US</a><a href="#">GIFT CARD</a>
  </nav>
  <div class="hero-caption">COME FISH WITH TAMPA BAY, FL FISHING GUIDE, TAMPA BAY FISHING CHARTER MOST RESPECTED CAPTAIN, 25 YEAR NATIVE GUIDE</div>
</header>

<section class="intro">
  <h1>TAMPA BAY, FISHING GUIDE, TAMPA BAY<br>FISHING CHARTERS</h1>
  <p>Capt. Wade Harlow, with over 20 years' experience, Native fishing charter tampa charter captain offering full and half day fishing charters on the waters of Tampa Bay.<br>
  If you're looking for a great fishing charter tampa don't hesitate to contact Capt. Wade or you can simply book your trip online <a href="#">here.</a><br>
  Come enjoy a wonderful day fishing charters Tampa for Tarpon, Snook, Redfish, Trout, Sharks, Cobia, Spanish mackerel as well as others aboard Capt. Wade Harlow Sport fishing Charters boat. Capt. Wade will work hard to ensure that you and your guests have a memorable day enjoying the wonderful gamefish that Tampa Bay has to offer.</p>
</section>

<section class="services" role="img" aria-label="Blue-tinted background photo of an angler on a boat">
  <article class="card charters">
    <h2>FULL &amp; HALF DAY CHARTERS</h2>
    <div class="card-photo" role="img" aria-label="Photo of anglers on a boat landing a large tarpon"></div>
    <p>Offering Tampa Bay, FL fishing charters on the beautiful waters of Tampa Bay. Fish with Capt. Wade Harlow, Tampa Bay, FL fishing guide for over 20 years</p>
    <span class="btn">&#8596; FIND OUT MORE</span>
  </article>
  <article class="card pickups">
    <h2>MULTIPLE PICKUP POINTS</h2>
    <div class="card-photo" role="img" aria-label="Photo of a smiling angler holding up a snook on the boat"></div>
    <p>Whether you're looking for a fishing charter/guide in Tampa, St. Pete, Clearwater or Bradenton, Capt. Wade can pick you up nearby.</p>
    <span class="btn">&#8596; MAPS &amp; PICKUP LOCATIONS</span>
  </article>
</section>

<footer class="footer">
  <div class="col contact">
    <h3>CONTACT US</h3>
    <div class="socials"><span aria-label="Quillbook">Q</span><span aria-label="Chirply">C</span><span aria-label="Vidora">V</span><span aria-label="Feed">R</span></div>
    <div class="line"><svg width="7" height="7" viewBox="0 0 24 24"><path d="M6 3l3 5-2 2c1 3 3 5 6 6l2-2 5 3-2 4C10 21 3 14 2 6z" fill="#fbf289"/></svg>555-014-2280</div>
    <div class="line"><svg width="8" height="6" viewBox="0 0 16 12"><rect width="16" height="12" fill="#fbf289"/><path d="M0 0l8 6 8-6" stroke="#0d1621" fill="none"/></svg>captwade@reelcove.example</div>
  </div>
  <span class="divider" style="left:193px"></span>
  <div class="col" style="left:226px">
    <h3>PICKUP LOCATIONS</h3>
    <ul class="pickup-list">
      <li>Pelican Point Marina - Seabreeze</li>
      <li>Heron Harbor - Driftwood</li>
      <li>Mangrove Boat Ramp</li>
      <li>Tarpon Key Boat Ramp</li>
    </ul>
  </div>
  <span class="divider" style="left:366px"></span>
  <div class="col news">
    <h3>NEWSLETTER SIGNUP</h3>
    <p>Come fish with Tampa Bay, FL fishing guide, Tampa Bay fishing charter most respected Captain, 25 year Native Guide</p>
    <div class="signup"><div class="email">Email Address</div><div class="submit">SUBMIT</div></div>
  </div>
</footer>

<div class="base">
  <div class="copyright">Copyright © 2016 Capt. Wade Harlow. All Right Reserved.</div>
  <div class="cards"><span>Cardo</span><span>Ringpay</span><span>Crest</span><span>Farpay</span></div>
</div>
</body>
</html>
```